I'm looking for a logo design however launched a business card design project and just bundled the logo design project.

Kindly submit a proposal for a logo and business card so I can pay you for both designs. Here are what I need.

Please see attachment for our current logo design.

We need double side design card for our website promotion.

Logo Text

Zunotrip482

```html
<!DOCTYPE html>
<html lang="en">
<head>
<meta charset="utf-8">
<title>Zunotrip482 Business Card</title>
<link href="https://fonts.googleapis.com/css2?family=Montserrat:wght@400;600;700&display=swap" rel="stylesheet">
<style>
  :root {
    --stage: #2a2a2a;
    --brand-blue: #256bb5;
    --ink-blue: #2161ae;
    --accent-orange: #f47a2a;
    --paper: #ffffff;
    --text: #333333;
    --map-tint: rgba(255,255,255,0.10);
  }
  * { margin: 0; padding: 0; box-sizing: border-box; }
  html, body { width: 1200px; height: 1022px; overflow: hidden; }
  body {
    background: var(--stage);
    font-family: "Montserrat", sans-serif;
    position: relative;
  }
  .card {
    position: absolute;
    left: 262px;
    width: 678px;
    height: 387px;
    overflow: hidden;
  }
  .card-front { top: 104px; background: var(--brand-blue); }
  .card-back { top: 530px; background: var(--paper); }

  .world-map {
    position: absolute;
    left: 24px; top: 36px;
    width: 630px; height: 318px;
    border-radius: 40% 45% 50% 40%;
    background: radial-gradient(ellipse at center, var(--map-tint) 0%, rgba(255,255,255,0.04) 60%, transparent 75%);
  }
  .front-mark {
    position: absolute;
    left: 276px; top: 93px;
    width: 130px; height: 130px;
    border-radius: 50%;
    background: var(--paper);
  }
  .front-name {
    position: absolute;
    left: 0; right: 0; top: 226px;
    text-align: center;
    color: var(--paper);
    font-weight: 600;
    font-size: 68px;
    letter-spacing: -1px;
  }

  .back-mark {
    position: absolute;
    left: 139px; top: 141px;
    width: 64px; height: 64px;
    border-radius: 50%;
    background: var(--ink-blue);
  }
  .back-name {
    position: absolute;
    left: 40px; width: 300px; top: 212px;
    text-align: center;
    color: var(--ink-blue);
    font-weight: 600;
    font-size: 40px;
    letter-spacing: -1px;
  }
  .divider {
    position: absolute;
    left: 338px; top: 85px;
    width: 2px; height: 218px;
    background: var(--ink-blue);
  }
  .details {
    position: absolute;
    left: 355px; top: 78px;
    color: var(--text);
    font-size: 18px;
  }
  .person-name {
    color: var(--ink-blue);
    font-weight: 700;
    font-size: 23px;
    letter-spacing: 0.5px;
    line-height: 28px;
  }
  .person-role { line-height: 22px; }
  .address { margin-top: 12px; line-height: 26px; }
  .contacts { list-style: none; margin-top: 12px; }
  .contacts li {
    display: flex; align-items: center;
    height: 26px;
  }
  .contacts svg { width: 15px; height: 15px; margin-right: 8px; flex: none; }
  .footer-band {
    position: absolute;
    left: 0; bottom: 0;
    width: 678px; height: 52px;
    background: linear-gradient(180deg, var(--paper) 0%, #f9c9a6 22%, var(--brand-blue) 60%, var(--brand-blue) 100%);
  }
</style>
</head>
<body>
  <section class="card card-front">
    <div class="world-map" role="img" aria-label="Dotted world map in a lighter blue"></div>
    <div class="front-mark"></div>
    <div class="front-name">Zunotrip482</div>
  </section>

  <section class="card card-back">
    <div class="back-mark"></div>
    <div class="back-name">Zunotrip482</div>
    <div class="divider"></div>
    <div class="details">
      <div class="person-name">DORIAN VELL</div>
      <div class="person-role">Owner</div>
      <div class="address">718 Larkmoor Ave. #45<br>Fenwick Hollow, CA. 90417</div>
      <ul class="contacts">
        <li>
          <svg viewBox="0 0 16 16"><rect x="4" y="1" width="8" height="14" rx="1.5" fill="none" stroke="#f47a2a" stroke-width="1.6"/><circle cx="8" cy="12.5" r="0.9" fill="#f47a2a"/></svg>
          555-204-7731
        </li>
        <li>
          <svg viewBox="0 0 16 16"><path d="M1 7c0-3 14-3 14 0v1h-3V6.5H4V8H1z" fill="#f47a2a"/><rect x="3" y="9" width="10" height="5" rx="1" fill="#f47a2a"/></svg>
          555-386-1142
        </li>
        <li>
          <svg viewBox="0 0 16 16"><rect x="1" y="3" width="14" height="10" fill="#f47a2a"/><path d="M1 3l7 6 7-6" fill="none" stroke="#fff" stroke-width="1.3"/></svg>
          hello@zunotrip482.com
        </li>
        <li>
          <svg viewBox="0 0 16 16"><circle cx="8" cy="8" r="7" fill="#f47a2a"/><path d="M1 8h14M8 1c-3 3-3 11 0 14M8 1c3 3 3 11 0 14" fill="none" stroke="#fff" stroke-width="1"/></svg>
          www.zunotrip482.com
        </li>
      </ul>
    </div>
    <div class="footer-band" role="img" aria-label="Decorative orange and blue wave band along the bottom edge"></div>
  </section>
</body>
</html>
```